Email signature and business card

Australian company called Tarrowin. We provide construction and maintenance services to the mining industry. I would like the design to be similar to our website theme(www.tarrowin.com.au) whilst staying compact. RGB colours to include: 42,96,140 and 232,163,0 and I have attached 2 logos.

The following fields will need to be included:

Full Name
Title
Location/Project
Phone
Mobile
Fax
Email
Web site

Target Market(s)

Mining Industry

Industry/Entity Type

Construction

Requirements
Must have
• Full Name, Title, Office Address, Phone, Mobile, Fax, Email, Web address
• Back of card must include: Boilermaking, Carpentry, Concrete, Construction, Cranes, Data and Comms, Electrical, Fabrication, Fitting, Labour Hire, Plumbing, Rigging, Shutdowns

```html
<!DOCTYPE html>
<html lang="en">
<head>
<meta charset="utf-8">
<title>Tarrowin Business Card</title>
<link rel="stylesheet" href="https://fonts.googleapis.com/css2?family=Arimo:ital,wght@0,400;0,700;1,400&display=swap">
<style>
  :root {
    --navy: #1f4a63;
    --blue: #2a608c;
    --orange: #e8a300;
    --pale: #dde9f1;
    --ink: #1d1d1d;
    --paper: #ffffff;
    --backdrop: #ecebe8;
    --ghost: #e4e6e8;
  }
  * { box-sizing: border-box; margin: 0; padding: 0; }
  html, body { width: 1200px; height: 1000px; overflow: hidden; }
  body {
    background: var(--backdrop);
    font-family: "Arimo", Arial, sans-serif;
    position: relative;
  }
  .card {
    position: absolute;
    width: 540px;
    height: 330px;
    background: var(--paper);
    box-shadow: 0 10px 28px rgba(0,0,0,0.18);
    overflow: hidden;
  }
  .card--front { left: 60px; top: 140px; }
  .card--back { left: 600px; top: 500px; }

  .card__web {
    position: absolute;
    top: 22px; right: 26px;
    color: var(--orange);
    font-weight: 700;
    font-size: 13px;
  }
  .brand {
    position: absolute;
    left: 36px; top: 46px;
    display: flex; align-items: center; gap: 10px;
  }
  .brand__dot {
    width: 38px; height: 38px; border-radius: 50%;
    background: var(--blue);
  }
  .brand__name {
    color: var(--blue);
    font-weight: 700;
    font-size: 22px;
    letter-spacing: 0.5px;
    text-transform: uppercase;
  }
  .card__band {
    position: absolute;
    left: 0; right: 0; top: 104px;
    height: 12px;
    background: var(--navy);
  }
  .card__lower {
    position: absolute;
    left: 0; right: 0; top: 116px; bottom: 0;
  }
  .card--front .card__lower { background: var(--pale); }
  .card__mark {
    position: absolute;
    right: 40px; top: 140px;
    width: 70px; height: 70px; border-radius: 50%;
    background: var(--ghost);
    opacity: 0.8;
  }

  .contact {
    position: absolute;
    left: 96px; top: 140px;
    color: var(--ink);
  }
  .contact__name {
    color: var(--orange);
    font-weight: 700;
    font-size: 15px;
    text-transform: uppercase;
    letter-spacing: 0.5px;
  }
  .contact__title { font-style: italic; font-size: 14px; margin-top: 2px; color: #333; }
  .contact__row { display: flex; gap: 22px; font-size: 14px; margin-top: 2px; }
  .contact__label { font-weight: 700; color: var(--navy); }
  .contact__address { font-size: 12px; margin-top: 18px; line-height: 1.3; }
  .contact__row--small { font-size: 12px; gap: 24px; margin-top: 0; }

  .services {
    position: absolute;
    left: 56px; top: 134px;
    right: 110px;
  }
  .services__heading {
    color: var(--navy);
    font-weight: 700;
    font-size: 15px;
    margin-bottom: 6px;
  }
  .services__columns { display: flex; gap: 34px; }
  .services__list { list-style: none; }
  .services__item {
    font-size: 13.5px;
    color: var(--ink);
    line-height: 26px;
    display: flex; align-items: center; gap: 14px;
  }
  .services__item::before {
    content: "";
    width: 9px; height: 9px;
    background: var(--orange);
    flex: none;
  }
  .services__list--second, .services__list--third { margin-top: -22px; }
</style>
</head>
<body>

<section class="card card--front" aria-label="Business card front">
  <div class="card__web">www.tarrowin.com.au</div>
  <div class="brand">
    <span class="brand__dot"></span>
    <span class="brand__name">Tarrowin</span>
  </div>
  <div class="card__band"></div>
  <div class="card__lower"></div>
  <div class="card__mark"></div>
  <div class="contact">
    <p class="contact__name">Mara Ellison</p>
    <p class="contact__title">Sales Consultant</p>
    <p class="contact__row">
      <span><span class="contact__label">M:</span> (07) 3100 4821</span>
      <span><span class="contact__label">E:</span> mara@tarrowin.com.au</span>
    </p>
    <p class="contact__address">Level 3, 14 Quarry Road<br>Brindle Bay QLD 4590</p>
    <p class="contact__row contact__row--small">
      <span><span class="contact__label">P:</span> (07) 3100 4800</span>
      <span><span class="contact__label">F:</span> (07) 3100 4899</span>
    </p>
  </div>
</section>

<section class="card card--back" aria-label="Business card back">
  <div class="card__web">www.tarrowin.com.au</div>
  <div class="brand">
    <span class="brand__dot"></span>
    <span class="brand__name">Tarrowin</span>
  </div>
  <div class="card__band"></div>
  <div class="card__mark"></div>
  <div class="services">
    <h2 class="services__heading">SERVICES:</h2>
    <div class="services__columns">
      <ul class="services__list">
        <li class="services__item">Boilermaking</li>
        <li class="services__item">Construction</li>
        <li class="services__item">Electrical</li>
        <li class="services__item">Labour Hire</li>
        <li class="services__item">Shutdowns</li>
      </ul>
      <ul class="services__list services__list--second">
        <li class="services__item">Carpentry</li>
        <li class="services__item">Cranes</li>
        <li class="services__item">Fabrication</li>
        <li class="services__item">Plumbing</li>
      </ul>
      <ul class="services__list services__list--third">
        <li class="services__item">Concrete</li>
        <li class="services__item">Data and Comm</li>
        <li class="services__item">Fitting</li>
        <li class="services__item">Rigging</li>
      </ul>
    </div>
  </div>
</section>

</body>
</html>
```